Velmora Beauty Sensitive Skin Intimate Shave Cream

We need a label/package design for a female shave cream. Our brand is Velmora Beauty and we manufacturer luxuriously sexy female intimate items. We are looking for sexy packaging to really get our brand out there. I have included in attachments, all of the files including font, logo, size requirements and verbage requirements. On the file "shave-cream-requirements" please use to format for size. Also on that file, I need the "must have" verbage from my project brief laid out exactly the same. The name of the product is Velmora Beauty Original Sexy Intimate Shave Cream
Target Market(s)
Females who like luxury and feeling sexy
Industry/Entity Type
Manufacturer
Requirements
Must have
- Must have my velmora beauty logo. The scent for this cream is called "Velvet Bloom" Please put that one the label. Also the actual scent is "an array of light florals with a hint of baby powder" please put that in small letters on back of the label
- Must be Label Dimensions: 6.25h X 7.375w
- Must say "Intimate Shave Cream for Her".
- Must say - Fill Weight: 16 Fl. Oz. (480ml) ℮
- must say - Suggested use: Apply intimate shave cream where desired and glide razor over skin for smooth results
- Must say - Ingredient Deck:
- Water (Eau/Aqua), Cetyl Alcohol, Cetrimonium Bromide, Stearyl Alcohol, Hydroxyethylcellulose, Glyceryl Stearate, PEG-100 Stearate, PEG-60 Lanolin, Simmondsia Chinensis (Jojoba) Seed Oil, Hydrolyzed Keratin, Panthenol, Allantoin, Phenoxyethanol, Methylisothiazolinone, Sodium Hydroxide, Fragrance (Parfum)
- Must say these cautions:
- Recommend Cautions:
- Do Not Use if You have a Known Hypersensitivity (Allergy) to Any of the Ingredients
- If Irritation Occurs, Discontinue Use
- If Eye Contact Occurs, Rinse with Water to Remove
- Keep Out of Reach of Children
- Must say : Specially formulated with skin soothing ingredients to provide a smooth and effortless shave.
- Protects and nourishes from irritation and razor cuts
- Helps prevent embarrassing shave rashes and ingrown hairs.
- Designed for sensitive and intimate skin. Perfect for intimate areas, legs, underarms, face, and body.
- Enhanced with hair and skin moisturizing agents.
- Can also be used to condition skin and hair after shampoo.
- Must have UPC (included) and part number:VQ583047 in small writing on the back of the label.
Should not have
- cheap looking designs and logos

```html
<!DOCTYPE html>
<html lang="en">
<head>
<meta charset="utf-8">
<title>Velmora Beauty Intimate Shave Cream – Label</title>
<link rel="stylesheet" href="https://fonts.googleapis.com/css2?family=Open+Sans:wght@400;600;700&family=Quicksand:wght@300;400&family=Josefin+Sans:wght@300&family=Playfair+Display:ital,wght@1,700&display=swap">
<style>
  :root{
    --page:#ffffff;
    --pink-top:#cf7eab;
    --pink-mid:#d6428a;
    --pink-deep:#8e1f57;
    --ink-light:#ffffff;
    --ink-soft:#f6e6ee;
    --silver-dark:#9a9a9a;
    --silver-light:#e6e6e6;
  }
  html,body{margin:0;padding:0;width:1200px;height:786px;overflow:hidden;background:var(--page);}
  .label{position:absolute;left:40px;top:51px;width:1120px;height:684px;}
  .label-face{
    position:absolute;left:0;top:0;width:1120px;height:655px;
    background:linear-gradient(180deg,var(--pink-top) 0%,var(--pink-mid) 50%,var(--pink-deep) 100%);
    color:var(--ink-light);
    font-family:"Open Sans",Arial,sans-serif;
  }
  .label-foil{
    position:absolute;left:0;top:655px;width:1120px;height:29px;
    background:linear-gradient(90deg,var(--silver-dark),var(--silver-light) 35%,#bdbdbd 60%,var(--silver-light) 80%,var(--silver-dark));
  }

  .back-panel{position:absolute;left:24px;width:175px;font-size:10.5px;line-height:15px;}
  .back-panel h3{margin:0;font-size:12.5px;font-weight:700;line-height:17px;}
  .back-panel p{margin:0;}
  .usage{top:56px;width:160px;font-size:12.5px;line-height:17px;}
  .ingredients{top:170px;}
  .ingredients h3{margin-bottom:3px;}
  .cautions{top:400px;left:27px;width:180px;font-size:12px;line-height:17.5px;}

  .claims{position:absolute;left:224px;top:0;width:48px;}
  .claim{position:absolute;left:0;width:48px;text-align:center;font-size:6.5px;line-height:8px;}
  .claim svg{display:block;margin:0 auto 3px;}

  .brand-rule{position:absolute;left:502px;top:55px;width:1.5px;height:590px;background:var(--ink-light);}
  .brand-name,.brand-tag{
    position:absolute;transform:translate(-50%,-50%) rotate(-90deg);
    white-space:nowrap;font-family:"Josefin Sans","Helvetica Neue",sans-serif;font-weight:300;
  }
  .brand-name{left:452px;top:300px;font-size:54px;letter-spacing:12px;}
  .brand-tag{left:528px;top:363px;font-size:20px;letter-spacing:15px;}

  .product-title{position:absolute;left:548px;top:238px;width:180px;text-align:center;font-family:"Quicksand",sans-serif;font-weight:300;}
  .product-title .kind{font-size:30px;font-weight:400;line-height:34px;}
  .product-title .type{font-size:24px;line-height:29px;}
  .scent-name{font-family:"Playfair Display",Georgia,serif;font-style:italic;font-weight:700;font-size:32px;line-height:40px;margin-top:14px;}

  .fill-weight{position:absolute;left:547px;top:608px;font-size:15px;}

  .front-copy{position:absolute;text-align:center;font-size:11.5px;line-height:17px;}
  .front-copy p{margin:0;}
  .benefits{left:900px;top:45px;width:195px;}
  .directions{left:950px;top:355px;width:148px;}
  .scent-notes{left:960px;top:460px;width:135px;}
  .part-info{position:absolute;left:955px;top:548px;width:150px;text-align:center;font-family:Arial,Helvetica,sans-serif;font-size:14px;line-height:18px;color:var(--ink-soft);}
</style>
</head>
<body>
<div class="label">
  <div class="label-face">

    <div class="back-panel usage">
      <h3>Suggested use:</h3>
      <p>Apply intimate shave cream where desired and glide razor over skin for smooth results</p>
    </div>

    <div class="back-panel ingredients">
      <h3>Ingredient :</h3>
      <p>Water (Eau/Aqua), Cetyl Alcohol, Cetrimonium Bromide, Stearyl Alcohol, Hydroxyethylcellulose, Glyceryl Stearate, PEG-100 Stearate, PEG-60 Lanolin, Simmondsia Chinensis (Jojoba) Seed Oil, Hydrolyzed Keratin, Panthenol, Allantoin, Phenoxyethanol, Methylisothiazolinone, Sodium Hydroxide, Fragrance (Parfum)</p>
    </div>

    <div class="back-panel cautions">
      <h3>Recommend Cautions:</h3>
      <p>Do Not Use if You have a Known Hypersensitivity (Allergy) to Any of the Ingredients.</p>
      <p>If Irritation Occurs, Discontinue Use.</p>
      <p>If Eye Contact Occurs, Rinse with Water to Remove.</p>
      <p>Keep Out of Reach of Children.</p>
    </div>

    <div class="claims">
      <div class="claim" style="top:52px">
        <svg width="40" height="24" viewBox="0 0 40 24"><rect x="1" y="1" width="38" height="22" fill="none" stroke="#fff" stroke-width="1.5"/><path d="M1 7H39M1 12H39M1 17H39" stroke="#fff" stroke-width="1.5"/></svg>
        Made in USA
      </div>
      <div class="claim" style="top:140px">
        <svg width="40" height="40" viewBox="0 0 40 40"><circle cx="20" cy="20" r="17" fill="#fff"/></svg>
        No Animal Testing
      </div>
      <div class="claim" style="top:252px">
        <svg width="40" height="40" viewBox="0 0 40 40"><circle cx="20" cy="20" r="17" fill="none" stroke="#fff" stroke-width="3"/></svg>
        Sugar-Free
      </div>
      <div class="claim" style="top:365px">
        <svg width="40" height="40" viewBox="0 0 40 40"><circle cx="20" cy="20" r="17" fill="none" stroke="#fff" stroke-width="1.5"/></svg>
        Safe For All Skin Types
      </div>
      <div class="claim" style="top:476px">
        <svg width="40" height="40" viewBox="0 0 40 40"><circle cx="20" cy="20" r="17" fill="none" stroke="#fff" stroke-width="3"/><circle cx="20" cy="20" r="10" fill="#fff"/></svg>
        Paraben-Free
      </div>
      <div class="claim" style="top:580px">
        <svg width="40" height="40" viewBox="0 0 40 40"><circle cx="20" cy="20" r="17" fill="none" stroke="#fff" stroke-width="3"/><path d="M8 32L32 8" stroke="#fff" stroke-width="3"/></svg>
        Sulfate-Free
      </div>
    </div>

    <div class="brand-name">VELMORA</div>
    <div class="brand-rule"></div>
    <div class="brand-tag">BEAUTY</div>

    <div class="product-title">
      <div class="kind">INTIMATE</div>
      <div class="type">Shave Cream</div>
      <div class="type">for Her</div>
      <div class="scent-name">Velvet<br>Bloom</div>
    </div>

    <div class="fill-weight">16 Fl. Oz. (480ml) ℮</div>

    <div class="front-copy benefits">
      <p>Specially formulated with skin soothing ingredients to provide a smooth and effortless shave.</p>
      <p>Protects and nourishes from irritation and razor cuts.</p>
      <p>Helps prevent embarrassing shave rashes and ingrown hairs..</p>
      <p>Designed for sensitive and intimate skin. Perfect for intimate areas, legs, underarms, face, and body.</p>
      <p>Enhanced with hair and skin moisturizing agents.</p>
      <p>Can also be used to condition skin and hair after shampoo.</p>
    </div>

    <div class="front-copy directions"><p>Apply intimate shave cream where desired and glide razor over skin for smooth results</p></div>

    <div class="front-copy scent-notes"><p>an array of light florals with a hint of baby powder</p></div>

    <div class="part-info">
      UnAssigned<br>
      Model: VQ583047<br>
      SKU: VQ583047
    </div>
  </div>
  <div class="label-foil"></div>
</div>
</body>
</html>
```